Business Cards for Tech Company - vLumowren

We would like new modern business cards designed for our company. Attached are some examples of other business cards we like. <br/><br/>Info we need is: <br/>First Name, Last Name<br/>Address<br/>Store Phone<br/>Cell Phone<br/>Email Address<br/>Text Logo <br/>And Other Logo<br/>

Industry/Entity Type

Technology Equipment

Contact Information for Business Card

Please use these details as example:

Brent Lodd
Technology Specialist
Direct 555.617.4089
Phone 555-730-1826

brent.lodd@vlumowren.example

6120 Tallis Lane
Harlow Bend, QX 00000

Font styles to use
Sans Serif
Other font styles liked:
• Anything easy to read and modern

Colors

Designer to choose colors to be used in the design.

Requirements
Must have
• Both Logos
• Signature as name
• Use the text logo and use the shark logo but do not use the full shark logo. Have it where it is zoomed in and is expanding out of the card.
Nice to have
• Keep it clean and modern
• We like blue, white, and black/grays.
Should not have
• Random icons for phone and address.

```html
<!DOCTYPE html>
<html lang="en">
<head>
<meta charset="UTF-8">
<title>vLumowren Business Cards</title>
<link href="https://fonts.googleapis.com/css2?family=Lato:wght@400;700;900&display=swap" rel="stylesheet">
<style>
  :root {
    --backdrop: #151515;
    --card-white: #ffffff;
    --blue-deep: #1477f0;
    --blue-light: #38b8f6;
    --brand-blue: #1a86f0;
    --ink-grey: #555a60;
    --ink-dark: #33363a;
    --rule-grey: #d2d4d7;
  }
  * { box-sizing: border-box; margin: 0; padding: 0; }
  html, body {
    width: 1200px;
    height: 900px;
    overflow: hidden;
    background: var(--backdrop);
    font-family: "Lato", Arial, sans-serif;
  }
  .stage {
    position: relative;
    width: 1200px;
    height: 900px;
    display: flex;
    flex-direction: column;
    align-items: center;
    justify-content: center;
    gap: 60px;
  }
  .card {
    width: 600px;
    height: 343px;
    position: relative;
    box-shadow: 0 18px 40px rgba(0, 0, 0, 0.55);
  }
  .card--front {
    background: linear-gradient(160deg, var(--blue-light) 0%, var(--blue-deep) 48%, var(--blue-light) 100%);
    display: flex;
    align-items: center;
    justify-content: center;
    gap: 14px;
  }
  .front-mark__dot {
    width: 30px;
    height: 30px;
    border-radius: 50%;
    background: var(--card-white);
  }
  .front-mark__name {
    color: var(--card-white);
    font-weight: 900;
    font-size: 40px;
    letter-spacing: -0.5px;
  }
  .card--back {
    background: var(--card-white);
  }
  .brand-name {
    position: absolute;
    left: 44px;
    top: 176px;
    color: var(--brand-blue);
    font-weight: 900;
    font-size: 46px;
    letter-spacing: -1px;
  }
  .divider {
    position: absolute;
    left: 318px;
    top: 0;
    width: 2px;
    height: 343px;
    background: linear-gradient(to bottom, rgba(210,212,215,0) 0%, var(--rule-grey) 45%, rgba(210,212,215,0) 100%);
  }
  .contact {
    position: absolute;
    left: 346px;
    top: 40px;
    color: var(--ink-dark);
    font-size: 16px;
    line-height: 1.32;
  }
  .contact__name {
    font-weight: 900;
    font-size: 22px;
    color: var(--ink-grey);
    line-height: 1.1;
  }
  .contact__name .surname { color: var(--brand-blue); }
  .contact__title {
    font-size: 15px;
    color: var(--ink-grey);
    margin-bottom: 14px;
  }
  .contact__label { color: var(--brand-blue); }
  .contact__address { margin-top: 16px; }
</style>
</head>
<body>
  <main class="stage">
    <section class="card card--front" aria-label="Business card front">
      <span class="front-mark__dot"></span>
      <span class="front-mark__name">vLumowren</span>
    </section>

    <section class="card card--back" aria-label="Business card back">
      <div class="brand-name">vLumowren</div>
      <div class="divider"></div>
      <div class="contact">
        <p class="contact__name">BRENT <span class="surname">LODD</span></p>
        <p class="contact__title">Technology Specialist</p>
        <p><span class="contact__label">Direct :</span> 555.617.4089</p>
        <p><span class="contact__label">Phone :</span> 555-730-1826</p>
        <p>brent.lodd@vlumowren.example</p>
        <p class="contact__address">6120 Tallis Lane<br>Harlow Bend, QX 00000</p>
      </div>
    </section>
  </main>
</body>
</html>
```